Design some Stationery for a Wedding Greeting Card - repost

I am looking for a Wedding Card to congratulate the Bride and Groom, it can be Modern, Contemporary or Traditional.
Can be 5 x 5 or 7 x 5 in size with [url removed, login to view] bleed. Must be a folded card not a flat card.
Can have text or not. Cannot have cut outs or layers. Can be coloured or traditional white.

```html
<!DOCTYPE html>
<html lang="en">
<head>
<meta charset="utf-8">
<title>Happy Wedding Greeting Card</title>
<link rel="stylesheet" href="https://fonts.googleapis.com/css2?family=Federo&family=Italianno&display=swap">
<style>
  :root {
    --backdrop: #efeff1;
    --cover-top: #d88aa5;
    --cover-bottom: #b04a72;
    --cloud: #ffffff;
    --lace: #1a1418;
    --ribbon: #f4f2f3;
    --ink-pink: #c4497a;
    --page: #ece9ea;
    --cake-top: #f1c6d6;
    --cake-bottom: #cf4a7e;
  }
  html, body {
    margin: 0;
    padding: 0;
    width: 1200px;
    height: 840px;
    overflow: hidden;
    background: var(--backdrop);
  }
  .canvas {
    position: relative;
    width: 1200px;
    height: 840px;
  }
  .panel {
    position: absolute;
    top: 140px;
    width: 400px;
    height: 560px;
    box-shadow: 0 6px 22px rgba(0,0,0,0.12);
  }
  .cover {
    left: 170px;
    background: linear-gradient(180deg, var(--cover-top), var(--cover-bottom));
  }
  .cover-cloud {
    position: absolute;
    left: 60px;
    top: 40px;
    width: 280px;
    height: 250px;
  }
  .cover-cake {
    position: absolute;
    left: 130px;
    top: 85px;
    width: 140px;
    height: 165px;
    border-radius: 10px 10px 6px 6px;
    background: linear-gradient(180deg, var(--cake-top), var(--cake-bottom));
  }
  .lace-band {
    position: absolute;
    left: 0;
    width: 400px;
    height: 24px;
    background: var(--lace);
  }
  .lace-band--top { top: 326px; }
  .lace-band--bottom { top: 424px; }
  .title-ribbon {
    position: absolute;
    left: 0;
    top: 350px;
    width: 400px;
    height: 74px;
    background: var(--ribbon);
    display: flex;
    align-items: center;
    justify-content: center;
  }
  .card-title {
    margin: 0;
    font-family: "Federo", sans-serif;
    font-weight: 400;
    font-size: 40px;
    letter-spacing: 1px;
    color: var(--ink-pink);
  }
  .inside {
    left: 630px;
    background: var(--page);
  }
  .inside-message {
    position: absolute;
    left: 50px;
    top: 110px;
    width: 300px;
    margin: 0;
    text-align: center;
    font-family: "Italianno", cursive;
    font-size: 27px;
    line-height: 1.05;
    color: var(--ink-pink);
  }
  .inside-cake {
    position: absolute;
    left: 170px;
    top: 330px;
    width: 60px;
    height: 70px;
    border-radius: 6px 6px 4px 4px;
    background: linear-gradient(180deg, var(--cake-top), var(--cake-bottom));
  }
</style>
</head>
<body>
<main class="canvas">
  <section class="panel cover" aria-label="Card front">
    <svg class="cover-cloud" viewBox="0 0 280 250" aria-hidden="true">
      <g fill="var(--cloud)">
        <circle cx="140" cy="60" r="55"/>
        <circle cx="75" cy="80" r="50"/>
        <circle cx="205" cy="80" r="50"/>
        <circle cx="55" cy="145" r="52"/>
        <circle cx="225" cy="145" r="52"/>
        <circle cx="90" cy="195" r="48"/>
        <circle cx="190" cy="195" r="48"/>
        <circle cx="140" cy="140" r="90"/>
      </g>
    </svg>
    <div class="cover-cake" role="img" aria-label="Illustration of a three-tier patterned wedding cake topped with two hearts"></div>
    <div class="lace-band lace-band--top" role="img" aria-label="Black lace trim"></div>
    <div class="title-ribbon">
      <h1 class="card-title">Happy Wedding</h1>
    </div>
    <div class="lace-band lace-band--bottom" role="img" aria-label="Black lace trim"></div>
  </section>

  <section class="panel inside" aria-label="Card inside">
    <p class="inside-message">Wishing you both great happiness and joy on your wedding day. We hope that it is something that you'll cherish for many years to come. All the very best and good luck for the future.</p>
    <div class="inside-cake" role="img" aria-label="Small illustration of a tiered wedding cake with two hearts"></div>
  </section>
</main>
</body>
</html>
```